Billboard Design for Harbor Lane Dentistry

Brookhaven Family Dental Care
Phone number: 318-562-0913
Address: 248 Castleford Blvd
Hours: 7am-5pm ; Monday-Friday

Dental Implant Surgery
Same Day Emergency Visits
Cosmetic Treatments
GLINT! Whitening

NAMES: Dr. Colin Varnstaad
Dr. Peter Ashdale

MOST INSURANCES ACCEPTED

Eye catching slogan/colors/design for billboard

Our website is www.brookhavenfamilydentalcare.example to see current branding.

Target Market(s)

Target market is anyone in Alexandria. Focus on Families and High End Cosmetic Dentistry.

Industry/Entity Type

Dental Clinic

Requirements
Must have
• Brookhaven Family Dental Care
• Phone number: 318-562-0913
• Address: 248 Castleford Blvd
• Hours: 7am-5pm ; Monday-Friday
• Dental Implant Surgery
• Same Day Emergency Visits
• Cosmetic Treatments
• GLINT! Whitening
• NAMES: Dr. Colin Varnstaad
• Dr. Peter Ashdale
• and logo
Nice to have
• digital billboard-try to catch attention with color or phrase
Should not have
• Can not make claims or compare to other area dentist's according to laws.

```html
<!DOCTYPE html>
<html lang="en">
<head>
<meta charset="utf-8">
<title>Brookhaven Family Dental Care – Billboard</title>
<link href="https://fonts.googleapis.com/css2?family=Montserrat:wght@400;500;600;700;800&display=swap" rel="stylesheet">
<style>
  :root {
    --page-bg: #eef1f4;
    --sky: #b9def2;
    --royal: #1b64b3;
    --navy-text: #1c5aa5;
    --teal: #46b6d4;
    --ink: #16202e;
    --white: #ffffff;
    --photo-bg: #eef0f2;
    --skin: #e9b79c;
    --skin-light: #f3d2bf;
    --hair-blonde: #d9c6a2;
    --hair-brown: #6d4b34;
  }
  * { box-sizing: border-box; margin: 0; padding: 0; }
  html, body {
    width: 1200px; height: 1000px; overflow: hidden;
    background: var(--page-bg);
    font-family: "Montserrat", Arial, sans-serif;
  }
  .billboard {
    position: absolute; left: 40px; top: 233px;
    width: 1120px; height: 533px;
    background: var(--white);
    overflow: hidden;
    box-shadow: 0 10px 30px rgba(0,0,0,.15);
  }
  .billboard__shapes { position: absolute; inset: 0; }
  .photo-area { position: absolute; left: 0; top: 0; width: 530px; height: 450px; }
  .brand {
    position: absolute; left: 30px; top: 428px; width: 400px;
    text-align: center; color: var(--teal); font-weight: 600;
  }
  .brand__name { font-size: 46px; letter-spacing: 2px; line-height: 1; }
  .brand__sub { font-size: 15px; letter-spacing: 7px; margin-top: 10px; }
  .doctors {
    position: absolute; left: 540px; right: 10px; top: 18px;
    text-align: center; color: var(--navy-text);
    font-size: 44px; line-height: 1.1; font-weight: 500;
  }
  .doctors strong { font-weight: 700; }
  .services {
    position: absolute; left: 500px; right: 20px; top: 158px;
    list-style: none; text-align: center; color: var(--white);
    font-size: 27px; font-weight: 500; letter-spacing: .5px; line-height: 36px;
  }
  .services li span { border-bottom: 2px solid var(--white); padding: 0 8px 1px; }
  .services li:last-child span { border-bottom: none; }
  .contact {
    position: absolute; left: 480px; right: 10px; top: 334px;
    text-align: center; color: var(--ink);
  }
  .contact__address { font-size: 27px; font-weight: 500; }
  .hours {
    display: inline-flex; margin-top: 6px; font-weight: 700; font-size: 29px;
  }
  .hours__label { background: var(--teal); color: var(--navy-text); padding: 3px 12px; }
  .hours__time { background: var(--royal); color: var(--white); padding: 3px 16px; }
  .contact__phone {
    margin-top: 4px; font-size: 50px; font-weight: 700; color: var(--navy-text);
    display: flex; align-items: center; justify-content: center; gap: 10px; line-height: 1.15;
  }
  .contact__phone svg { width: 38px; height: 38px; }
  .contact__web { font-size: 23px; font-weight: 700; }
</style>
</head>
<body>
  <section class="billboard">
    <svg class="photo-area" viewBox="0 0 530 450" role="img" aria-label="Photo of a smiling young couple, cheek to cheek">
      <defs>
        <linearGradient id="photoBase" x1="0" y1="0" x2="0" y2="1">
          <stop offset="0" stop-color="var(--photo-bg)"/>
          <stop offset=".7" stop-color="#f6f7f8"/>
          <stop offset="1" stop-color="#ffffff"/>
        </linearGradient>
        <radialGradient id="toneLeft" cx=".5" cy=".5" r=".5">
          <stop offset="0" stop-color="var(--skin-light)"/>
          <stop offset=".55" stop-color="var(--hair-blonde)" stop-opacity=".8"/>
          <stop offset="1" stop-color="var(--hair-blonde)" stop-opacity="0"/>
        </radialGradient>
        <radialGradient id="toneRight" cx=".5" cy=".5" r=".5">
          <stop offset="0" stop-color="var(--skin)"/>
          <stop offset=".6" stop-color="var(--skin)" stop-opacity=".7"/>
          <stop offset="1" stop-color="var(--skin)" stop-opacity="0"/>
        </radialGradient>
        <radialGradient id="toneHair" cx=".5" cy=".5" r=".5">
          <stop offset="0" stop-color="var(--hair-brown)" stop-opacity=".85"/>
          <stop offset="1" stop-color="var(--hair-brown)" stop-opacity="0"/>
        </radialGradient>
        <linearGradient id="fadeOut" x1="0" y1="0" x2="0" y2="1">
          <stop offset=".55" stop-color="#ffffff" stop-opacity="0"/>
          <stop offset=".95" stop-color="#ffffff" stop-opacity="1"/>
        </linearGradient>
        <clipPath id="photoClip"><polygon points="0,0 500,0 445,450 0,450"/></clipPath>
      </defs>
      <g clip-path="url(#photoClip)">
        <rect width="530" height="450" fill="url(#photoBase)"/>
        <ellipse cx="190" cy="230" rx="190" ry="230" fill="url(#toneLeft)"/>
        <ellipse cx="380" cy="70" rx="150" ry="90" fill="url(#toneHair)"/>
        <ellipse cx="370" cy="220" rx="150" ry="190" fill="url(#toneRight)"/>
        <rect width="530" height="450" fill="url(#fadeOut)"/>
      </g>
    </svg>

    <svg class="billboard__shapes" viewBox="0 0 1120 533" width="1120" height="533" aria-hidden="true">
      <polygon points="520,0 1120,0 1120,146 500,146" fill="var(--sky)"/>
      <polygon points="470,146 1120,146 1120,309 450,309" fill="var(--royal)"/>
      <polygon points="480,309 1120,309 1120,533 455,533" fill="var(--sky)"/>
      <polygon points="500,0 526,0 456,533 430,533" fill="var(--royal)"/>
    </svg>

    <div class="brand">
      <div class="brand__name">BROOKHAVEN</div>
      <div class="brand__sub">FAMILY DENTAL CARE</div>
    </div>

    <h1 class="doctors">
      DR. COLIN <strong>VARNSTAAD</strong><br>
      DR. PETER <strong>ASHDALE</strong>
    </h1>

    <ul class="services">
      <li><span>DENTAL IMPLANT SURGERY</span></li>
      <li><span>SAME DAY EMERGENCY VISITS</span></li>
      <li><span>COSMETIC TREATMENTS</span></li>
      <li><span>GLINT! WHITENING</span></li>
    </ul>

    <div class="contact">
      <p class="contact__address">248 CASTLEFORD BLVD</p>
      <p class="hours"><span class="hours__label">HOURS</span><span class="hours__time">7AM-5PM ; MONDAY-FRIDAY</span></p>
      <p class="contact__phone">
        <svg viewBox="0 0 24 24" aria-hidden="true"><path fill="var(--ink)" d="M6.6 10.8a15.1 15.1 0 0 0 6.6 6.6l2.2-2.2c.3-.3.7-.4 1-.2 1.1.4 2.3.6 3.6.6.6 0 1 .4 1 1V20c0 .6-.4 1-1 1A17 17 0 0 1 3 4c0-.6.4-1 1-1h3.5c.6 0 1 .4 1 1 0 1.3.2 2.5.6 3.6.1.3 0 .7-.2 1l-2.3 2.2z"/></svg>
        318-562-0913
      </p>
      <p class="contact__web">www.brookhavenfamilydentalcare.example</p>
    </div>
  </section>
</body>
</html>
```